Pictures required on web page

I would like change three existing pictures on my new website.

The site can be found here:
http://maplebarrelvaults.quillstudio.com.au/

The three pictures to be changed are on the home page:
Purchase- Mixed Packs
Wine Club - Let Us Choose
Education- Wine Courses

I would like somthing stylish, classic and understated that fits in with the theme and feel of the site. I know stylish is a subjective thing. At the moment, the current picture makes the text difficult to read on a destop. Plus I don't think they are a perfect fit for our website anyway. I've attached a photo of our wine course room and also me in the store. Please, don't feel as though you have to use these pictures, but they're there if you want them. However I'm open to completely different photos/graphics to be used.

```html
<!DOCTYPE html>
<html lang="en">
<head>
<meta charset="utf-8">
<title>Maplebarrel – Small winery specialist</title>
<link rel="stylesheet" href="https://fonts.googleapis.com/css2?family=Roboto:wght@400;500&family=Roboto+Slab:wght@300..700&family=Teko:wght@500;600&display=swap">
<style>
:root{
  --header-top:#25355a;
  --header-bottom:#1c2946;
  --nav-bg:#151d2c;
  --page-bg:#ffffff;
  --text-light:#ffffff;
  --text-soft:#c9d3e6;
  --search-bg:#344672;
  --search-border:#7f90b8;
  --divider:#3b4b70;
  --shipping-red:#b24646;
  --newsletter-navy:#223253;
  --frame-line:rgba(255,255,255,.45);
  --accent-orange:#ff5a16;
  --accent-red:#e3262b;
  --accent-yellow:#f4b41a;
}
*{box-sizing:border-box;margin:0;padding:0}
html,body{width:1200px;height:478px;overflow:hidden;background:var(--page-bg)}
body{font-family:"Roboto",sans-serif;color:var(--text-light);position:relative}

.site-header{position:absolute;left:0;top:0;width:1200px;height:83px;background:linear-gradient(var(--header-top),var(--header-bottom))}
.brand{position:absolute;left:190px;top:10px}
.brand-name{font-family:"Roboto Slab","Rockwell",serif;font-weight:700;font-size:32px;line-height:34px;letter-spacing:-.3px}
.brand-tagline{font-family:"Roboto Slab","Rockwell",serif;font-weight:300;font-size:14.5px;color:var(--text-soft);line-height:18px}

.search{position:absolute;left:430px;top:23px;width:248px;height:28px;background:var(--search-bg);border:1px solid var(--search-border);border-radius:3px;display:flex;align-items:center;padding-left:11px;font-size:13px;color:var(--text-soft)}
.search svg{position:absolute;right:8px;top:3px}

.utility-nav{position:absolute;left:703px;top:17px;display:flex}
.utility-item{width:68.5px;height:38px;display:flex;flex-direction:column;align-items:center;justify-content:space-between;font-size:10.5px;color:var(--text-soft);border-left:1px solid var(--divider)}
.utility-item:first-child{border-left:none}
.utility-item svg{fill:var(--text-soft)}

.category-nav{position:absolute;left:0;top:83px;width:1200px;height:41px;background:var(--nav-bg)}
.category-list{position:absolute;left:191px;top:10px;display:flex;gap:26px;list-style:none;font-size:15.5px;font-weight:500}
.cart{position:absolute;left:907px;top:10px;display:flex;align-items:center;gap:7px;font-size:11px}

.tile{position:absolute;overflow:hidden;display:block}
.photo{position:absolute;inset:0}
.tile-caption{position:absolute;left:0;right:0;text-align:center;font-family:"Teko",sans-serif;line-height:.85;text-transform:uppercase;text-shadow:0 2px 6px rgba(0,0,0,.55)}
.caption-kicker{font-size:22px;font-weight:500;color:var(--text-light)}
.caption-title{font-size:45px;font-weight:600}

.tile-course{left:172px;top:134px;width:284px;height:195px}
.tile-course .photo{background:
  radial-gradient(ellipse 30% 22% at 57% 24%,rgba(255,214,150,.55),transparent 70%),
  radial-gradient(ellipse 90% 55% at 50% 30%,#8a5a32 0%,#5c3a20 55%,transparent 100%),
  linear-gradient(180deg,#4a2c18 0%,#3a2214 60%,#24150c 100%)}
.tile-course .tile-caption{top:131px}
.tile-course .caption-title{color:var(--accent-orange)}

.tile-club{left:465px;top:134px;width:290px;height:332px}
.tile-club .photo{background:
  radial-gradient(ellipse 45% 30% at 30% 45%,rgba(210,214,226,.6),transparent 70%),
  linear-gradient(180deg,#b7bac6 0%,#8990a8 35%,#4a5483 70%,#1e2a66 100%)}
.tile-club .tile-caption{top:34px}
.tile-club .caption-title{color:var(--accent-red);font-size:41px}
.read-more{position:absolute;right:16px;bottom:14px;width:75px;height:21px;border:1px solid var(--frame-line);font-family:"Roboto Slab","Rockwell",serif;font-size:9.5px;display:flex;align-items:center;justify-content:center;letter-spacing:.3px}

.tile-packs{left:765px;top:134px;width:287px;height:198px}
.tile-packs .photo{background:
  radial-gradient(ellipse 35% 45% at 22% 40%,rgba(150,140,130,.55),transparent 70%),
  radial-gradient(ellipse 50% 70% at 80% 45%,#6e2e24 0%,transparent 80%),
  linear-gradient(180deg,#3e1e18 0%,#52261e 50%,#24110e 100%)}
.tile-packs .tile-caption{top:134px}
.tile-packs .caption-title{color:var(--accent-yellow)}

.promo{position:absolute;display:flex;align-items:center;justify-content:center}
.promo-frame{position:absolute;inset:18px 17px;border:1px solid var(--frame-line)}
.promo-text{position:relative;text-align:center}
.promo-title{font-size:17px;letter-spacing:1.6px;font-weight:400}
.promo-sub{font-family:"Roboto Slab","Rockwell",serif;font-weight:400;font-size:11.5px;letter-spacing:1px;margin-top:4px}
.promo-shipping{left:174px;top:337px;width:280px;height:127px;background:var(--shipping-red)}
.promo-newsletter{left:770px;top:335px;width:280px;height:127px;background:var(--newsletter-navy)}
</style>
</head>
<body>

<header class="site-header">
  <div class="brand">
    <div class="brand-name">Maplebarrel</div>
    <div class="brand-tagline">Small winery specialist.</div>
  </div>

  <div class="search">Search the Cellars
    <svg width="20" height="20" viewBox="0 0 20 20" fill="none" stroke="#e6ebf5" stroke-width="2"><circle cx="8" cy="8" r="6"/><line x1="12.5" y1="12.5" x2="18" y2="18" stroke-width="2.6"/></svg>
  </div>

  <nav class="utility-nav">
    <div class="utility-item"><svg width="14" height="13" viewBox="0 0 14 13"><path d="M7 0 0 6h2v7h4V9h2v4h4V6h2z"/></svg>HOME</div>
    <div class="utility-item"><svg width="18" height="13" viewBox="0 0 18 13"><circle cx="9" cy="3" r="3"/><circle cx="3.5" cy="4.5" r="2.2"/><circle cx="14.5" cy="4.5" r="2.2"/><path d="M4 13c0-4 2-6 5-6s5 2 5 6z"/><path d="M0 12c0-3 1.5-4.5 3.5-4.5S6 8 6 9v3z"/><path d="M18 12c0-3-1.5-4.5-3.5-4.5S12 8 12 9v3z"/></svg>ABOUT</div>
    <div class="utility-item"><svg width="13" height="14" viewBox="0 0 13 14"><path d="M0 2h13v12H0zM1.5 5v7.5h10V5z"/><rect x="3" y="0" width="1.5" height="3"/><rect x="8.5" y="0" width="1.5" height="3"/></svg>EVENTS</div>
    <div class="utility-item"><svg width="14" height="14" viewBox="0 0 14 14"><path d="M6 0h2l.4 2 1.6.7 1.7-1.2 1.4 1.4-1.2 1.7.7 1.6 2 .4v2l-2 .4-.7 1.6 1.2 1.7-1.4 1.4-1.7-1.2-1.6.7L8 14H6l-.4-2-1.6-.7-1.7 1.2-1.4-1.4 1.2-1.7L1.4 8 0 8V6l2-.4.7-1.6L1.5 2.3 2.9.9 4.6 2.1 6.2 1.4zM7 4.6A2.4 2.4 0 1 0 7 9.4 2.4 2.4 0 0 0 7 4.6z"/></svg>ACCOUNT</div>
    <div class="utility-item"><svg width="13" height="13" viewBox="0 0 13 13"><path d="M2.5 0 5 2.7 3.6 4.6c.9 1.9 2.8 3.8 4.8 4.8L10.3 8 13 10.5 11 13C5 12.5.5 8 0 2z"/></svg>CONTACT</div>
  </nav>
</header>

<nav class="category-nav">
  <ul class="category-list">
    <li>Red Wine</li><li>White Wine</li><li>Sparkling</li><li>Rosé</li><li>Stickies</li><li>Imported</li><li>Wine Club</li>
  </ul>
  <div class="cart">
    <svg width="22" height="18" viewBox="0 0 22 18" fill="#fff"><path d="M0 0h4l1 3h17l-3 8H7l.6 2H19v2H6L2.5 2H0z"/><circle cx="8" cy="16.5" r="1.5"/><circle cx="17" cy="16.5" r="1.5"/></svg>
    Shopping cart is empty
  </div>
</nav>

<main>
  <a class="tile tile-course">
    <div class="photo" role="img" aria-label="Warmly lit wine course room with a long table and shelves of bottles"></div>
    <div class="tile-caption"><div class="caption-kicker">Education</div><div class="caption-title">Wine Course</div></div>
  </a>

  <div class="promo promo-shipping">
    <div class="promo-frame"></div>
    <div class="promo-text"><div class="promo-title">FREE SHIPPING</div><div class="promo-sub">on orders over $200</div></div>
  </div>

  <a class="tile tile-club">
    <div class="photo" role="img" aria-label="Blue-toned shopfront of the wine store with the owner standing in the doorway"></div>
    <div class="tile-caption"><div class="caption-kicker">Wine Club</div><div class="caption-title">Let Us Choose</div></div>
    <div class="read-more">READ MORE</div>
  </a>

  <a class="tile tile-packs">
    <div class="photo" role="img" aria-label="Store owner leaning on a ladder beside shelves of red wine"></div>
    <div class="tile-caption"><div class="caption-kicker">Purchase</div><div class="caption-title">Mixed Packs</div></div>
  </a>

  <div class="promo promo-newsletter">
    <div class="promo-frame"></div>
    <div class="promo-text"><div class="promo-title">NEWSLETTER</div><div class="promo-sub">join the newsletter for specials</div></div>
  </div>
</main>

</body>
</html>
```